Funky Entertainment and Music Solutions Company

Marlo Tindell Entertainment (www.marlotindell-example.com) needs a fresh new face. We are in Entertainment and Music Solutions for corporate and private functions providing a very hands-on and customer focused premium approach to our client's entertainment needs.

Current Logo:
It's the MARLO TINDELL ENTERTAINMENT found on our website above

What do we do?
We advise, organise, source and manage your event (big or small) from a string quartet for a cocktail party to pre-dinner entertainment and big band entertainment for the corporate Christmas Party.

Our Objective:
To become the main Entertainment and Music Solutions provider to large Australia/Asia Pac corporations as well as private parties.

Look and Feel?
We have recently released our new services booklet found here: http://www.pagewhirl-example.com/3A51B2C0F4D/q2mz84xr and whilst we don't want the site to look like a rainbow, it should incorporate the sleek, funky, clean look that we're tying to achieve.

Main pages we're after:
- Welcome/About Us
- Services (ie, strings, Covers Bands, Jazz Groups. All found in above booklet)
- Enquiry/Booking Page
- Gallery and Audio Page
Updates

This project now has a committed budget - submit away!
Thanks all!
Marlo Tindell Entertainment

Just a few updates on the project.
- We are trying to move away from what the current website offers. Our new client focus is corporate and private parties, not nightclubs. A great example are the images on the first and last pages of the flipbook: http://www.pagewhirl-example.com/3A51B2C0F4D/q2mz84xr
- Some websites that we like are found below. They are sleek, easy to navigate and not too much scrolling required. They incorporate a cool background with the floating ttext/images in the centre.
http://lanternhall-sf.example.com/
http://www.orbvale-example.com/
- Any questions, please ask!
Thanks and happy designing! :)

Industry/Entity Type

Entertainment

```html
<!DOCTYPE html>
<html lang="en">
<head>
<meta charset="utf-8">
<title>Marlo Tindell Entertainment</title>
<link rel="stylesheet" href="https://fonts.googleapis.com/css2?family=Carlito:ital,wght@0,400;0,700;1,400&family=Nunito:wght@700;800&display=swap">
<style>
:root{
  --wood-dark:#3a2216;
  --wood-mid:#6b4330;
  --wood-light:#8a5a40;
  --frame:#e4e4e4;
  --panel:#0d0c0e;
  --purple:#8a76e6;
  --text:#ffffff;
  --lamp:#fff3d6;
  --amber:#d98a2a;
}
*{margin:0;padding:0;box-sizing:border-box}
html,body{width:1200px;height:1000px;overflow:hidden}
body{
  position:relative;
  font-family:"Carlito",Calibri,sans-serif;
  color:var(--text);
  background:
    repeating-linear-gradient(90deg,rgba(0,0,0,.28) 0 3px,transparent 3px 118px),
    linear-gradient(90deg,var(--wood-dark),var(--wood-mid) 20%,var(--wood-light) 45%,var(--wood-mid) 70%,var(--wood-dark));
}
.print{position:absolute;background:#fff;padding:10px;border-radius:6px;box-shadow:0 6px 18px rgba(0,0,0,.45)}
.print .photo{width:100%;height:100%}
.print-a{left:90px;top:150px;width:420px;height:660px;transform:rotate(-7deg)}
.print-a .photo{background:linear-gradient(160deg,#6a57b8,#2b2348 40%,#1a1620)}
.print-b{left:640px;top:75px;width:440px;height:330px;transform:rotate(5deg)}
.print-b .photo{background:linear-gradient(150deg,#cfd6cf,#7c8a7c 50%,#3d443d)}
.print-c{left:600px;top:520px;width:540px;height:330px;transform:rotate(-3deg)}
.print-c .photo{background:linear-gradient(120deg,#3a3336,#8d7d72 55%,#c9bfb6)}
.print-d{left:150px;top:560px;width:480px;height:260px;transform:rotate(-2deg)}
.print-d .photo{background:linear-gradient(120deg,#262226,#5a5054)}

.site{position:absolute;left:160px;top:55px;width:882px;height:740px;border:8px solid var(--frame);border-radius:10px;background:rgba(13,12,14,.9);overflow:hidden}
.brand{position:absolute;left:12px;top:18px;font-family:"Carlito",sans-serif;font-weight:700;color:#d9d9d9;line-height:.95;letter-spacing:1px}
.brand .line1{font-size:42px}
.brand .line2{font-size:32px}
.nav{position:absolute;left:343px;top:73px;display:flex;gap:5px}
.nav a,.tile h3{font-family:"Nunito",sans-serif;font-weight:800;color:#fff;letter-spacing:-.5px;
  text-shadow:-1px -1px 0 #333,1px -1px 0 #333,-1px 1px 0 #333,1px 1px 0 #333,0 2px 3px rgba(0,0,0,.6)}
.nav a{display:block;height:43px;background:var(--purple);border-radius:16px 16px 0 0;text-decoration:none;font-size:24px;text-align:center;line-height:48px}

.hero{position:absolute;left:0;top:115px;width:577px;height:382px;
  background:
    radial-gradient(ellipse 42px 48px at 30px 40px,var(--lamp),rgba(255,220,150,.6) 55%,transparent 80%),
    radial-gradient(ellipse 48px 50px at 118px 44px,var(--lamp),rgba(255,220,150,.6) 55%,transparent 80%),
    radial-gradient(ellipse 50px 52px at 212px 46px,var(--lamp),rgba(255,220,150,.6) 55%,transparent 80%),
    radial-gradient(ellipse 50px 52px at 300px 46px,var(--lamp),rgba(255,220,150,.6) 55%,transparent 80%),
    radial-gradient(ellipse 48px 50px at 392px 44px,var(--lamp),rgba(255,220,150,.6) 55%,transparent 80%),
    radial-gradient(ellipse 44px 48px at 484px 42px,var(--lamp),rgba(255,220,150,.6) 55%,transparent 80%),
    radial-gradient(ellipse 120px 40px at 320px 140px,rgba(230,170,110,.55),transparent 75%),
    radial-gradient(ellipse 60px 140px at 75px 270px,rgba(235,235,235,.45),transparent 80%),
    radial-gradient(ellipse 65px 140px at 190px 260px,rgba(235,235,235,.45),transparent 80%),
    radial-gradient(ellipse 70px 150px at 330px 290px,rgba(20,18,20,.85),transparent 80%),
    radial-gradient(ellipse 60px 140px at 510px 270px,rgba(230,230,230,.4),transparent 80%),
    linear-gradient(180deg,#8a4a1c 0%,#b0602a 14%,#6a2e1a 30%,#3a2620 50%,#231b1a 75%,#151213)}
.hero-note{position:absolute;right:10px;top:8px;font-style:italic;font-size:14px;color:#111}
.about{position:absolute;left:584px;top:118px;width:275px;font-size:13px;line-height:17.25px;text-align:justify}
.about h2{font-size:13px;font-weight:700;margin-bottom:17px}
.about p{margin-bottom:17px}
.about p.indent{text-indent:32px}
.quote-bg{position:absolute;left:0;top:497px;width:577px;height:228px;background:linear-gradient(90deg,rgba(60,55,58,.55),rgba(30,28,30,.35))}
.quote{position:absolute;left:25px;top:520px;width:527px;font-style:italic;font-size:17px;line-height:21.6px;text-align:center}
.quote p+p{margin-top:22px}

.tile{position:absolute;top:818px;width:280px;height:200px;border:8px solid var(--frame);border-bottom:none;border-radius:8px 8px 0 0;background:#222}
.tile h3{height:46px;background:var(--purple);font-size:27px;text-align:right;padding-right:12px;line-height:50px}
.tile .thumb{height:140px}
.tile-events{left:160px}
.tile-events .thumb{background:linear-gradient(160deg,#3a3030,#6e5a4a 50%,#221b1b)}
.tile-bands{left:459px}
.tile-bands .thumb{background:linear-gradient(160deg,#2e4f86,#1b2a48 55%,#101218)}
.tile-videos{left:757px}
.tile-videos .thumb{position:relative;background:linear-gradient(160deg,#b88a3a,#7a5420 60%,#3a2810)}
.play{position:absolute;left:110px;top:50px}
</style>
</head>
<body>
  <div class="print print-a"><div class="photo" role="img" aria-label="Event venue lit in purple"></div></div>
  <div class="print print-b"><div class="photo" role="img" aria-label="Outdoor garden function"></div></div>
  <div class="print print-c"><div class="photo" role="img" aria-label="String musician performing at a function"></div></div>
  <div class="print print-d"><div class="photo" role="img" aria-label="Band on stage"></div></div>

  <main class="site">
    <div class="brand"><div class="line1">MARLO TINDELL</div><div class="line2">ENTERTAINMENT</div></div>
    <nav class="nav">
      <a href="#" style="width:123px">Home</a>
      <a href="#" style="width:126px">Services</a>
      <a href="#" style="width:124px">Bookings</a>
      <a href="#" style="width:123px">Gallery</a>
    </nav>

    <div class="hero" role="img" aria-label="Four-piece band in white shirts and ties posing under warm stage lamps">
      <span class="hero-note">(flash slide show - changing images)</span>
    </div>

    <section class="about">
      <h2>A new take on the event scene</h2>
      <p class="indent">Marlo Tindell Entertainment has been bringing a touch of class to functions around Australia and the Asia Pacific for over a decade. Planning every event down to the smallest detail ensures that your next function will run smoothly so you can relax and enjoy. With a start to finish approach, MTE prides itself on client collaboration and event experience to produce unique and memorable events, talked about long after your last guest has left.</p>
      <p class="indent">Marlo Tindell is a talented and passionate musician which, when combined with his extensive knowledge of the current music and events scene, enables him to offer clients completely unique and tailor made music and event experiences. In addition to working as a booking agent and behind the scenes, Marlo is on-stage with almost every performance. His unique ability to combine his superb saxophone skills with live DJ'ing is not only a rare occurrence in this industry today but has audiences captivated from start to end, and clients coming back for more.</p>
      <p>With an impressive list of clientele throughout Australia and the Asia-Pacific region Marlo Tindell Entertainment has established a trusted and well respected reputation within the event and music industries. Previous clients include Halvern Hotels, Invitely, Southern Skyways, Lumacharm Singapore, Jade Lantern Room, Dockside, Fernhouse, and Harbourline Bar.</p>
    </section>

    <div class="quote-bg" role="img" aria-label="Faded photo of musicians performing"></div>
    <blockquote class="quote">
      <p>“Marlo Tindell Entertainment is a unique live performance and event solutions provider offering a premium service and a highly customisable approach to event and entertainment management.</p>
      <p>With over a decade of experience and a long list of artists to choose from, we can guarantee that every detail is catered for. Contact us at info@marlotindell-example.com to see how we can ensure your next event is a success!”</p>
    </blockquote>
  </main>

  <section class="tile tile-events"><h3>Events</h3><div class="thumb" role="img" aria-label="Saxophonist playing among dancing guests"></div></section>
  <section class="tile tile-bands"><h3>Bands</h3><div class="thumb" role="img" aria-label="Big band brass section seated in a hall"></div></section>
  <section class="tile tile-videos"><h3>Videos</h3>
    <div class="thumb" role="img" aria-label="Video still of a town band performance">
      <svg class="play" width="44" height="32" viewBox="0 0 44 32"><rect x="1" y="1" width="42" height="30" rx="5" fill="#555" stroke="#ddd" stroke-width="2"/><path d="M18 9 L30 16 L18 23 Z" fill="#fff"/></svg>
    </div>
  </section>
</body>
</html>
```